Stationery Design Project - Ta fourmilière

We are a french company, Ta Fourmilière. It means Your Anthill.
We own and manage woods, we transform it industrially into very high quality (dry) logs and pellets and we commercialize them to individuals in France.
People can order the logs online or by phone and get the wood logs delivered at home.

After our great logo contest, we would like to launch a new stationery project.

Target Market(s)

inhabitants of sub-urban areas in France. (living in houses not in apartment )

Industry/Entity Type

It Company

Requirements
Must have
• content see attachment
logo

For the business card, we would like on the front side, the logo, name + contact info. We would like to use the back side for commercial purpose insisting on our distinctive value proposition.
Nice to have
• the back side of the business card can be more colorful

```html
<!DOCTYPE html>
<html lang="fr">
<head>
<meta charset="utf-8">
<title>Ta Fourmilière — Papeterie</title>
<link rel="stylesheet" href="https://fonts.googleapis.com/css2?family=Roboto+Condensed:wght@700&display=swap">
<style>
  :root{
    --bg:#ebe9e6;
    --paper:#ffffff;
    --red:#c01f26;
    --charcoal:#404040;
    --yellow:#f5c11a;
    --wood-light:#efe8df;
    --wood-dark:#d8cdbf;
    --illustration:#b9906c;
  }
  html,body{margin:0;padding:0;overflow:hidden;}
  body{width:1200px;height:1048px;background:var(--bg);position:relative;
       font-family:"Roboto Condensed",Arial Narrow,sans-serif;font-weight:700;}
  .sheet{position:absolute;display:block;filter:drop-shadow(2px 3px 4px rgba(0,0,0,.25));}
  .letterhead{left:89px;top:72px;}
  .card-front{left:797px;top:583px;}
  .card-back{left:978px;top:583px;}
  svg text{font-family:"Roboto Condensed",Arial Narrow,sans-serif;font-weight:700;}
</style>
</head>
<body>

<svg class="sheet letterhead" width="631" height="893" viewBox="0 0 631 893" aria-label="Papier à en-tête Ta Fourmilière">
  <defs>
    <linearGradient id="woodFill" x1="0" y1="0" x2="0" y2="1">
      <stop offset="0" stop-color="var(--wood-light)"/>
      <stop offset="1" stop-color="var(--wood-dark)"/>
    </linearGradient>
    <path id="addressCurve" d="M50 860 Q316 718 585 850"/>
  </defs>
  <rect class="paper" width="631" height="893" fill="var(--paper)"/>
  <path class="header-band" d="M0 0 H631 V58 Q315 212 0 78 Z" fill="var(--red)"/>
  <circle class="logo-disc" cx="316" cy="133" r="106" fill="var(--paper)"/>
  <rect class="mascot" role="img" aria-label="Illustration du bûcheron tenant un plateau de bûches" x="275" y="38" width="110" height="78" rx="6" fill="var(--illustration)"/>
  <text class="brand-name" x="316" y="137" text-anchor="middle" font-size="30" fill="var(--charcoal)">Ta Fourmilière</text>

  <path class="wood-pile" role="img" aria-label="Illustration de bûches de bois empilées" d="M0 670 L105 595 L250 700 L390 650 L520 640 L631 710 V893 H0 Z" fill="url(#woodFill)"/>
  <path class="footer-band" d="M10 893 Q316 760 631 893 Z" fill="var(--charcoal)"/>
  <text class="footer-address" font-size="14.5" fill="var(--red)">
    <textPath href="#addressCurve" startOffset="50%" text-anchor="middle">12 Chemin des Pins,  69340 Francheville,  Tél : 04 72 10 20 30, info@tafourmiliere.fr</textPath>
  </text>
  <text class="footer-url" x="316" y="860" text-anchor="middle" font-size="16" fill="#fff">www.tafourmiliere.fr</text>
</svg>

<svg class="sheet card-front" width="151" height="270" viewBox="0 0 151 270" aria-label="Carte de visite, recto">
  <rect width="151" height="270" fill="var(--charcoal)"/>
  <circle class="logo-disc" cx="75" cy="80" r="58" fill="var(--paper)"/>
  <rect class="mascot" role="img" aria-label="Illustration du bûcheron" x="52" y="30" width="50" height="38" rx="4" fill="var(--illustration)"/>
  <path class="wood-band" role="img" aria-label="Illustration de bûches" d="M0 95 L30 92 L60 100 L110 92 L151 98 V185 H0 Z" fill="url(#woodFill)"/>
  <text class="brand-name" x="75" y="84" text-anchor="middle" font-size="17" fill="var(--charcoal)">Ta Fourmilière</text>
  <text class="tagline" x="75" y="126" text-anchor="middle" font-size="11.5" fill="var(--charcoal)">Entre nous, ça chauffe !</text>
  <rect class="url-tag" x="22" y="134" width="106" height="17" fill="var(--yellow)"/>
  <text x="75" y="146" text-anchor="middle" font-size="9.5" fill="var(--charcoal)">www.tafourmiliere.fr</text>
  <path class="contact-band" d="M0 180 Q75 165 151 180 V270 H0 Z" fill="var(--red)"/>
  <g class="contact" font-size="10.5" fill="#fff" text-anchor="middle">
    <text x="75" y="195">Paul-Henri MARCHAL</text>
    <text x="75" y="212">Tél : 04 72 10 20 30</text>
    <text x="75" y="230">Mobile : 04 72 10 20 30</text>
    <text x="75" y="247">marchal@tafourmiliere.fr</text>
  </g>
</svg>

<svg class="sheet card-back" width="152" height="270" viewBox="0 0 152 270" aria-label="Carte de visite, verso">
  <defs><clipPath id="backClip"><rect width="152" height="270"/></clipPath></defs>
  <g clip-path="url(#backClip)">
    <rect width="152" height="270" fill="url(#woodFill)"/>
    <path class="offer-band" d="M0 0 H152 V82 Q76 100 0 90 Z" fill="var(--red)"/>
    <g class="offer" font-size="11" fill="#fff" text-anchor="middle">
      <text x="76" y="28">Livraison gratuite de</text>
      <text x="76" y="45">bois de chauffage à Lyon</text>
      <text x="76" y="62">et sa région</text>
    </g>
    <g class="order" fill="var(--charcoal)" text-anchor="middle">
      <text x="76" y="111" font-size="10">Commandez sur</text>
      <text x="76" y="126" font-size="11.5">www.tafourmiliere.fr</text>
      <text x="76" y="139" font-size="10">ou au</text>
    </g>
    <rect class="phone-tag" x="28" y="144" width="96" height="19" fill="var(--yellow)"/>
    <text x="76" y="158" text-anchor="middle" font-size="12.5" fill="var(--charcoal)">04 72 10 20 30</text>
    <path class="promise-band" d="M0 180 Q76 163 152 180 V270 H0 Z" fill="var(--charcoal)"/>
    <g class="promise" font-size="10" fill="#fff" text-anchor="middle">
      <text x="64" y="188">Qualité</text>
      <text x="64" y="203">supérieure,</text>
      <text x="56" y="218">origine régionale</text>
      <text x="54" y="233">certifiée, livraison</text>
      <text x="91" y="248">en</text>
    </g>
    <circle class="delay-badge" cx="144" cy="262" r="40" fill="var(--yellow)"/>
    <text x="124" y="248" text-anchor="middle" font-size="18" fill="var(--red)">48h</text>
  </g>
</svg>

</body>
</html>
```